Album art cover

Album art design concept, my band will be releasing a 11 song rock album in the next few Months. We will be using it as a CD cover, poster, online art cover, maybe even Vinyl. Working album titles are "Copper in the rain" (Preferred album title) or "A lantern under the tide". Anything abstract, painting-like design, or whatever type of design that comes to mind. Fonts are designers choice. Thank You

Target Market(s)

Music business

Colors

Designer to choose colors to be used in the design.

Requirements
Must have
• Our band logo
Nice to have
• Anything abstract, attractive painting type, maybe even some kind of a futuristic design.
Should not have
• Skulls, blood-like, scary designs, nudity, emo type of design

```html
<!DOCTYPE html>
<html lang="en">
<head>
<meta charset="utf-8">
<title>A Lantern Under the Tide — Album Cover</title>
<link rel="stylesheet" href="https://fonts.googleapis.com/css2?family=Bebas+Neue&display=swap">
<style>
  :root {
    --page: #f5f4f6;
    --night: #2b1f3a;
    --violet: #5a3f8c;
    --lilac: #b49be0;
    --ember: #e0694e;
    --cyan: #3fc4f0;
    --ring: #9ff0ff;
    --ink: #ffffff;
    --accent: #e0356e;
  }
  * { box-sizing: border-box; margin: 0; padding: 0; }
  html, body {
    width: 1200px;
    height: 960px;
    overflow: hidden;
    background: var(--page);
  }
  .cover {
    position: absolute;
    left: 170px;
    top: 50px;
    width: 860px;
    height: 860px;
    overflow: hidden;
    background: var(--night);
    box-shadow: 0 8px 18px rgba(40, 25, 60, 0.25);
  }
  .cover__art {
    position: absolute;
    inset: 0;
    background:
      radial-gradient(ellipse 26% 12% at 30% 28%, rgba(224,105,78,0.75), transparent 70%),
      radial-gradient(ellipse 14% 16% at 58% 18%, rgba(224,105,78,0.6), transparent 70%),
      radial-gradient(ellipse 22% 12% at 22% 52%, rgba(224,105,78,0.5), transparent 70%),
      radial-gradient(ellipse 24% 12% at 80% 42%, rgba(63,196,240,0.6), transparent 70%),
      radial-gradient(ellipse 26% 10% at 82% 62%, rgba(63,196,240,0.55), transparent 70%),
      radial-gradient(ellipse 20% 10% at 74% 74%, rgba(224,105,78,0.4), transparent 70%),
      radial-gradient(ellipse 60% 60% at 50% 50%, rgba(90,63,140,0.6), transparent 80%),
      radial-gradient(ellipse 70% 70% at 0% 0%, rgba(180,155,224,0.55), transparent 60%),
      radial-gradient(ellipse 60% 70% at 0% 100%, rgba(180,155,224,0.5), transparent 60%),
      linear-gradient(160deg, #4a3466 0%, var(--night) 45%, #3a2a63 100%);
  }
  .cover__portrait {
    position: absolute;
    left: 188px;
    top: 184px;
    width: 484px;
    height: 484px;
    border-radius: 50%;
    background:
      radial-gradient(circle at 58% 22%, #6e6a78 0%, #3d3646 22%, transparent 40%),
      radial-gradient(ellipse 60% 55% at 42% 48%, #8c879e 0%, #5a5470 45%, transparent 75%),
      radial-gradient(circle at 50% 60%, #1d1622 0%, #0f0b14 100%);
  }
  .cover__ring {
    position: absolute;
    left: 158px;
    top: 154px;
    width: 544px;
    height: 544px;
  }
  .cover__title {
    position: absolute;
    left: 0;
    right: 0;
    top: 530px;
    text-align: center;
    font-family: "Bebas Neue", "Oswald", sans-serif;
    font-size: 60px;
    line-height: 60px;
    letter-spacing: 2px;
    color: var(--ink);
    text-shadow: 0 2px 6px rgba(0,0,0,0.7);
  }
  .band {
    position: absolute;
    left: 0;
    right: 0;
    top: 690px;
    display: flex;
    justify-content: center;
    align-items: center;
    gap: 10px;
  }
  .band__name {
    font-family: "Bebas Neue", "Oswald", sans-serif;
    font-size: 26px;
    letter-spacing: 4px;
    color: var(--ink);
  }
  .band__mark {
    width: 18px;
    height: 26px;
    border: 2px solid var(--accent);
  }
</style>
</head>
<body>
  <main class="cover">
    <div class="cover__art" role="img" aria-label="Abstract bursts of ember-red and cyan powder exploding outward on a grainy violet night backdrop"></div>
    <div class="cover__portrait" role="img" aria-label="Photograph of an outstretched hand reaching toward the viewer with a figure behind it, framed in a portal"></div>
    <svg class="cover__ring" viewBox="0 0 544 544" aria-hidden="true">
      <defs>
        <filter id="ring-glow" x="-20%" y="-20%" width="140%" height="140%">
          <feGaussianBlur stdDeviation="8" result="blur"/>
          <feMerge><feMergeNode in="blur"/><feMergeNode in="SourceGraphic"/></feMerge>
        </filter>
      </defs>
      <circle cx="272" cy="272" r="244" fill="none" stroke="var(--cyan)" stroke-width="10" opacity="0.6" filter="url(#ring-glow)"/>
      <circle cx="272" cy="272" r="244" fill="none" stroke="var(--ring)" stroke-width="4"/>
    </svg>
    <h1 class="cover__title">A Lantern<br>Under the Tide</h1>
    <div class="band">
      <span class="band__name">Harbor Static</span>
      <span class="band__mark"></span>
    </div>
  </main>
</body>
</html>
```